Business Card for Childrens Book Publisher

Would like a business card that reflects a newly established boutique childrens publishing company. The first project is a book to help raise children's self esteem titled "We Dance Till Noon." To get a better idea of the type of look I am after go to te website www.Wedancetillnoon.example.au. You can take the images from the book and use them for the business card. Would like it to have a fun innovative look and feel to it. The business is about being uplifting and positive for children, but also creating beautiful, high quality books. You can use whatever images you see on the website but I have more high res files that I can send to you over drop box or some other programs if you need them.I would like the business card to be two sided.

The information on the business card is:

Marble Lantern Books
Greta Malloway
Publisher/Author

Marble Lantern Books
marble lanterns glowing bright
T 0491 356 207
Po Box 64, Fernhill Rise, Vic 3019, Australia
ABN: 36 517 904 128
gretamalloway@marblelanternbooks.example
www.marblelanternbooks.example

Target Market(s)

Booksellers, parents, schools, kindergartens, owners of children's boutiques, retailers.

Industry/Entity Type

Boutique

Requirements
Must have
• Would it to be double sided.

```html
<!DOCTYPE html>
<html lang="en">
<head>
<meta charset="utf-8">
<title>Marble Lantern Books – Business Card</title>
<link rel="stylesheet" href="https://fonts.googleapis.com/css2?family=Open+Sans:ital,wght@0,400;0,600;0,700;0,800;1,400&family=Sniglet&display=swap">
<style>
  :root {
    --page-bg: #e9e9e9;
    --brand-blue: #1ba6de;
    --name-red: #e8452c;
    --title-red: #e0402a;
    --grass-light: #8fcc55;
    --grass-dark: #4caa3a;
    --white: #ffffff;
    --night-top: #1f3f9e;
    --night-mid: #2e62b8;
    --tagline-blue: #6ed3f4;
    --land-green: #5fb546;
    --sea-blue: #2a8fc9;
  }
  * { margin: 0; padding: 0; box-sizing: border-box; }
  html, body { width: 1200px; height: 695px; overflow: hidden; }
  body {
    background: var(--page-bg);
    font-family: "Open Sans", Arial, sans-serif;
    position: relative;
  }
  .card {
    position: absolute;
    top: 204px;
    width: 494px;
    height: 282px;
    border-radius: 14px;
    overflow: hidden;
  }
  /* Front */
  .card--front { left: 104px; background: var(--white); }
  .card--front .grass {
    position: absolute; left: 0; right: 0; top: 140px; bottom: 0;
    background: linear-gradient(180deg, var(--grass-light) 0%, #72bd48 45%, var(--grass-dark) 100%);
  }
  .card--front .artwork {
    position: absolute; left: 270px; top: 0; width: 224px; height: 140px;
    background: linear-gradient(200deg, #ffffff 0%, #fde9c8 30%, #f7b2a0 55%, #b9ddf2 75%, #ffffff 100%);
    opacity: .85;
  }
  .company {
    position: absolute; left: 24px; top: 30px;
    color: var(--brand-blue); font-size: 18px; font-weight: 400; letter-spacing: .2px;
    white-space: nowrap;
  }
  .person-name {
    position: absolute; left: 23px; top: 48px;
    color: var(--name-red); font-size: 30px; font-weight: 800; letter-spacing: .5px;
    word-spacing: 6px; white-space: nowrap;
  }
  .person-title {
    position: absolute; left: 24px; top: 89px;
    color: var(--title-red); font-size: 13px; font-style: italic;
  }
  .contact {
    position: absolute; top: 176px; color: var(--white);
    font-size: 12.5px; line-height: 18px; white-space: nowrap;
  }
  .contact--main { left: 22px; }
  .contact--main .label { display: inline-block; width: 14px; }
  .contact--post { left: 330px; }
  .divider {
    position: absolute; left: 318px; top: 174px; width: 2px; height: 58px; background: var(--white);
  }
  .abn {
    position: absolute; left: 0; right: 0; top: 255px; text-align: center;
    color: var(--white); font-size: 9px;
  }
  /* Back */
  .card--back {
    left: 617px;
    background: radial-gradient(ellipse at 50% 120%, var(--night-mid) 0%, var(--night-top) 70%);
  }
  .card--back .scene-sky { position: absolute; inset: 0; }
  .card--back .landscape {
    position: absolute; left: 0; right: 0; top: 196px; bottom: 0;
    background: linear-gradient(180deg, var(--sea-blue) 0%, #3fa4b0 35%, var(--land-green) 60%, #3f9a3c 100%);
  }
  .tagline {
    position: absolute; left: 0; right: 0; top: 92px; text-align: center;
    font-family: "Sniglet", "Comic Sans MS", cursive;
    color: var(--tagline-blue); font-size: 28px; letter-spacing: .3px; white-space: nowrap;
  }
  .back-url {
    position: absolute; left: 0; right: 0; top: 128px; text-align: center;
    color: var(--white); font-size: 18px; white-space: nowrap;
  }
</style>
</head>
<body>
  <section class="card card--front" aria-label="Business card front">
    <div class="grass"></div>
    <div class="artwork" role="img" aria-label="Illustration of two children playing beside a rainbow"></div>
    <p class="company">MARBLE LANTERN BOOKS</p>
    <h1 class="person-name">GRETA MALLOWAY</h1>
    <p class="person-title">Publisher/Author</p>
    <div class="contact contact--main">
      <p><span class="label">P</span>0491 356 207</p>
      <p><span class="label">E</span>gretamalloway@marblelanternbooks.example</p>
      <p>www.marblelanternbooks.example</p>
    </div>
    <div class="divider"></div>
    <div class="contact contact--post">
      <p>PO Box 64</p>
      <p>Fernhill Rise, VIC 3019</p>
      <p>Australia</p>
    </div>
    <p class="abn">ABN: 36 517 904 128</p>
  </section>

  <section class="card card--back" aria-label="Business card back">
    <div class="scene-sky" role="img" aria-label="Illustrated starry night sky"></div>
    <div class="landscape" role="img" aria-label="Illustration of green hills around a blue bay"></div>
    <p class="tagline">Marble lanterns glowing bright</p>
    <p class="back-url">www.marblelanternbooks.example</p>
  </section>
</body>
</html>
```